Business card Zottelgarten

Business card is for a self-employed dog trainer with own dog school. Name and logo of the dog school are available. Color specifications as well. The design should be classy and minimalist, but also modern. An already existing idea would be: Front: Only the logo Back: Contact data

Font styles to use
Serif
Sans Serif
Other font styles liked:
• Trajan Pro

Colors
f78f20

Requirements
Must have
• Name: Margit Wendler-Rasch Title: Dipl. Dog Trainer Contain my logo Follow my font and color preferences (see files)

```html
<!DOCTYPE html>
<html lang="en">
<head>
<meta charset="utf-8">
<title>Zottelgarten – Business Card</title>
<link rel="stylesheet" href="https://fonts.googleapis.com/css2?family=Cinzel:wght@400;600&family=Crimson+Text:wght@400&display=swap">
<style>
  :root {
    --backdrop: #2b2a29;
    --card-white: #f3f3f2;
    --card-brown: #776453;
    --ink-brown: #6e5a4a;
    --ink-body: #4f4a46;
    --accent-orange: #f08a1c;
    --rule: #6a6560;
    --white: #f6f4f1;
  }
  * { margin: 0; padding: 0; box-sizing: border-box; }
  html, body { width: 1200px; height: 960px; overflow: hidden; }
  body { background: var(--backdrop); position: relative; font-family: "Crimson Text", Georgia, serif; }

  .card { position: absolute; width: 600px; height: 343px; }
  .card--contact { left: 314px; top: 113px; background: var(--card-white); }
  .card--brand { left: 311px; top: 472px; background: var(--card-brown); }

  .person { position: absolute; left: 58px; top: 114px; }
  .person__name { font-family: "Cinzel", "Times New Roman", serif; font-weight: 600; font-size: 18px; color: var(--ink-brown); letter-spacing: 0.2px; line-height: 22px; }
  .person__title { font-family: "Cinzel", "Times New Roman", serif; font-size: 13.5px; color: var(--accent-orange); line-height: 20px; letter-spacing: 0.4px; }
  .person__address { font-size: 14px; color: var(--ink-body); line-height: 18px; margin-top: 3px; font-style: normal; }

  .contacts { position: absolute; left: 382px; top: 116px; list-style: none; }
  .contacts li { display: flex; align-items: center; height: 19px; font-size: 14px; color: var(--ink-body); }
  .contacts svg { width: 13px; height: 13px; margin-right: 9px; fill: var(--ink-body); flex: none; }

  .card__rule { position: absolute; left: 56px; top: 264px; width: 487px; height: 1px; background: var(--rule); }
  .card__web { position: absolute; left: 0; right: 0; top: 290px; text-align: center; font-size: 13px; letter-spacing: 4px; color: var(--ink-body); }

  .brand { position: absolute; left: 0; right: 0; top: 81px; text-align: center; }
  .brand__dot { display: block; width: 138px; height: 138px; margin: 0 auto; border-radius: 50%; background: var(--white); }
  .brand__name { font-family: "Cinzel", "Times New Roman", serif; font-weight: 400; font-size: 27px; color: var(--white); letter-spacing: 0.5px; line-height: 30px; margin-top: 6px; }
  .brand__web { font-family: "Cinzel", "Times New Roman", serif; font-size: 8.5px; color: var(--white); letter-spacing: 4px; line-height: 10px; }
</style>
</head>
<body>

<section class="card card--contact">
  <div class="person">
    <h1 class="person__name">MARGIT WENDLER-RASCH</h1>
    <p class="person__title">DIPL. DOG TRAINER</p>
    <address class="person__address">2214 Juniper Lane<br>Fairbanks, Alaska 99701</address>
  </div>

  <ul class="contacts">
    <li><svg viewBox="0 0 16 16" aria-hidden="true"><path d="M3.5 1l2.5 3-1.5 2c1 2 3 4 5 5l2-1.5 3 2.5-1.5 2.5C8 15 1 8 1 2.5z"/></svg>614 270 3851</li>
    <li><svg viewBox="0 0 16 16" aria-hidden="true"><path d="M4 0h8a1 1 0 0 1 1 1v14a1 1 0 0 1-1 1H4a1 1 0 0 1-1-1V1a1 1 0 0 1 1-1zm1 2v10h6V2zm3 11a1 1 0 1 0 0 2 1 1 0 0 0 0-2z"/></svg>772 519 0463</li>
    <li><svg viewBox="0 0 16 16" aria-hidden="true"><path d="M4 1h8v4H4zM1 6h14v7h-2v2H3v-2H1zm4 5v3h6v-3zM12 8a1 1 0 1 0 0 .1z"/></svg>395 148 6027</li>
    <li><svg viewBox="0 0 16 16" aria-hidden="true"><path d="M1 3h14v10H1zm1.5 1.2L8 8.5l5.5-4.3V4h-11z"/></svg>margit@zottelgarten.ch</li>
  </ul>

  <div class="card__rule"></div>
  <p class="card__web">www.zottelgarten.ch</p>
</section>

<section class="card card--brand">
  <div class="brand">
    <span class="brand__dot"></span>
    <p class="brand__name">ZOTTELGARTEN</p>
    <p class="brand__web">WWW.ZOTTELGARTEN.CH</p>
  </div>
</section>

</body>
</html>
```